Label for new gin: Kelm7 - Distilled Gin

Artistic label with local elements for new gin brand.
Dunes, lighthouses, sea, seagulls, ships.
Fresh lemon gin with fine juniper notes. Manufactured directly on the Baltic Sea in Warnemünde. Should be scalable. 4x6inch or larger.
Motifs put together artistically. Photos of the place in the attachment. The name of the gin comes from the beach entrance 3 (hence dune 3). A dune stalk (blue oat) is in the bottle. Bottle will be a clear glass apothecary bottle 500ml.

Niedrige Design-Qualität

Target Market(s)

spirits

Industry/Entity Type

Getränke

Font styles to use
Decorative
Script

Colors

Designer to choose colors to be used in the design.

Requirements
Must have
• Sketch, Handdrawn Style /// 500ml, 41% vol Alc "Made by QBAT GmbH Fasanring 27c Roggentin" "Bottled in Warnemünde" "Kelm7" "Distilled Gin" "Inspired by the sea"

```html
<!DOCTYPE html>
<html lang="de">
<head>
<meta charset="utf-8">
<title>Kelm7 - Distilled Gin</title>
<link href="https://fonts.googleapis.com/css2?family=Italiana&family=Cinzel:wght@400;600&family=Allura&display=swap" rel="stylesheet">
<style>
  :root {
    --backdrop: #161616;
    --paper: #f3f3f1;
    --ink: #141414;
    --amber: #d9954a;
    --band: #eeaa5e;
    --sky: #dcdcda;
    --town: #a9a9a7;
    --water: #6a6a68;
    --water-deep: #474747;
    --gull-tone: #d6d6d4;
    --white: #f5f5f5;
  }
  html, body {
    margin: 0;
    width: 900px;
    height: 1200px;
    overflow: hidden;
    background: var(--backdrop);
  }
  .label {
    position: absolute;
    left: 70px;
    top: 30px;
    width: 760px;
    height: 1140px;
    background: var(--paper);
    overflow: hidden;
  }
  .brand {
    position: absolute;
    top: 112px;
    margin: 0;
    width: 100%;
    text-align: center;
    font-family: "Italiana", serif;
    font-weight: 400;
    font-size: 132px;
    line-height: 1;
    letter-spacing: 16px;
    padding-left: 16px;
    box-sizing: border-box;
    color: var(--ink);
  }
  .kind {
    position: absolute;
    top: 284px;
    width: 100%;
    text-align: center;
    font-family: "Cinzel", serif;
    font-weight: 400;
    font-size: 40px;
    line-height: 1;
    letter-spacing: 7px;
    padding-left: 7px;
    box-sizing: border-box;
    color: var(--amber);
  }
  .spirit {
    position: absolute;
    top: 352px;
    width: 100%;
    text-align: center;
    font-family: "Italiana", serif;
    font-size: 152px;
    line-height: 1;
    color: var(--amber);
  }
  .tagline {
    position: absolute;
    top: 516px;
    width: 100%;
    text-align: center;
    font-family: "Allura", cursive;
    font-size: 52px;
    line-height: 1;
    color: var(--ink);
  }
  .origin {
    position: absolute;
    top: 588px;
    width: 100%;
    text-align: center;
    font-family: "Cinzel", serif;
    font-weight: 600;
    font-size: 18px;
    line-height: 1;
    letter-spacing: 3px;
    color: var(--ink);
  }
  .gull {
    position: absolute;
    background: var(--gull-tone);
    border-radius: 6px;
  }
  .gull--left { left: 74px; top: 258px; width: 94px; height: 56px; }
  .gull--right { left: 569px; top: 432px; width: 134px; height: 83px; }
  .harbour {
    position: absolute;
    left: 0;
    top: 575px;
    width: 100%;
    height: 515px;
    background: linear-gradient(to bottom,
      rgba(220,220,218,0) 0%,
      var(--sky) 8%,
      var(--town) 30%,
      var(--water) 55%,
      var(--water-deep) 100%);
  }
  .specs {
    position: absolute;
    top: 962px;
    width: 100%;
    text-align: center;
    font-family: "Cinzel", serif;
    font-size: 22px;
    letter-spacing: 4px;
    line-height: 49px;
    color: var(--white);
  }
  .maker {
    position: absolute;
    left: 0;
    bottom: 0;
    width: 100%;
    height: 51px;
    background: var(--band);
    font-family: "Cinzel", serif;
    font-weight: 600;
    font-size: 14px;
    letter-spacing: 6.5px;
    line-height: 51px;
    text-align: center;
    color: var(--ink);
  }
</style>
</head>
<body>
  <main class="label">
    <div class="harbour" role="img" aria-label="Pencil sketch of Warnemünde harbour with lighthouse, houses and fishing boats"></div>
    <div class="gull gull--left" role="img" aria-label="Sketched seagull in flight"></div>
    <div class="gull gull--right" role="img" aria-label="Sketched seagull in flight"></div>
    <h1 class="brand">KELM7</h1>
    <div class="kind">DISTILLED</div>
    <div class="spirit">GIN</div>
    <div class="tagline">Inspired by the sea</div>
    <div class="origin">BOTTLED IN WARNEMÜNDE</div>
    <div class="specs">500ML ℮<br>41% VOL ALC</div>
    <footer class="maker">MADE BY QBAT GMBH FASANRING 27C ROGGENTIN</footer>
  </main>
</body>
</html>
```